Plump Oscar's Terrier Store - balms

We are looking for a logo design for our new Bulldog butter tins and website. Inspired by our little fat bulldog Oscar who has very sensitive skin issues we have scoured the earth to find something for him - turns out only the most natural of ingredients suits our boy so we set out to get something made just for him. All natural, all organic and want to share it with other dogs and their mums and dads.

Oscar is a red and white bulldog and we really would like a design that is as close to resembling him as possible. See logo image below - but with Oscar and smiling! Essential the face markings are captured as much as possible (e.g. the dot on his head, eye patch etc). Options to see either just face or something similar to the pic titled Plump Oscar.

Important to convey natural and organic colouring. Organic type symbol.

Classy upmarket look. Eyecatching. Strong branding potential. see the meadow hound bazaar http://meadowhoundbazaar.example/shop/ as an example of simple but classy.

Logo to include wording Plump Oscar, 100% Natural & Organic, Bulldog Balm.

Some photos included below of Oscar. Can also be seen on instagram @plumposcartheterrier.

Tin will be similar to surfers wax - Dad is a surfer and so is Oscar! Rectangular. Estimated dimensions 110mmx80mmx25mm (see similar image).
Thank you!

Target Market(s)

Pet owners who adore their pet babies!

Industry/Entity Type

Shop

Requirements
Must have
• Be designed for a rectangular tin Estimated dimensions 110mmx80mmx25mm. Landscape view
• Organic logo (see file upload) located in corner.
• Net Wt 50gm
• Classy upmarket look but simple. Eyecatching. Not too cartoonish.
• Logo to include wording Plump Oscar, 100% Organic, Skin Balm
• Must capture Oscar's facemarkings - dot on head, eye patch, dots around nose and mouth.
• Key colours of Oscar (reddy-brown & tan /black and white) - probably don't want too many other colours - keep simple and classy
• Looking for a coloured background for the label - potentially same colour as Oscar to give a kind of a natural feel.
Should not have
• design for a round tin

```html
<!DOCTYPE html>
<html lang="en">
<head>
<meta charset="utf-8">
<title>Plump Oscar Skin Balm – Tin Label</title>
<link rel="stylesheet" href="https://fonts.googleapis.com/css2?family=Chewy&family=Bangers&family=Ultra&display=block">
<style>
  :root {
    --stage: #8f8e8e;
    --sheet: #ffffff;
    --brown: #5a3716;
    --lime: #d4e021;
    --green: #00923f;
    --green-deep: #217a3c;
    --badge-edge: #6aa532;
    --white: #ffffff;
  }
  html, body {
    margin: 0;
    width: 1200px;
    height: 1000px;
    overflow: hidden;
    background: var(--stage);
  }
  .label-art {
    display: block;
    width: 1200px;
    height: 1000px;
  }
  .sheet { fill: var(--sheet); }
  .frame-brown { fill: var(--brown); }
  .frame-lime { fill: var(--lime); }
  .field { fill: var(--green); }
  .ring-brown { fill: var(--brown); }
  .ring-lime { fill: var(--lime); }
  .portrait { fill: url(#portraitTone); }
  .seal { fill: var(--brown); }
  .seal-text {
    font-family: "Bangers", "Impact", sans-serif;
    font-size: 62px;
    fill: var(--lime);
    letter-spacing: 1px;
  }
  .cert-badge {
    fill: var(--white);
    stroke: var(--badge-edge);
    stroke-width: 2;
  }
  .brand-name {
    font-family: "Chewy", "Bangers", "Impact", sans-serif;
    font-size: 136px;
    fill: var(--white);
    stroke: var(--brown);
    stroke-width: 16px;
    stroke-linejoin: round;
    paint-order: stroke fill;
  }
  .product-name {
    font-family: "Ultra", "Bangers", "Impact", sans-serif;
    font-size: 34px;
    fill: var(--lime);
    stroke: var(--green-deep);
    stroke-width: 3px;
    paint-order: stroke fill;
  }
</style>
</head>
<body>
<svg class="label-art" viewBox="0 0 1200 1000" xmlns="http://www.w3.org/2000/svg">
  <defs>
    <radialGradient id="portraitTone" cx="50%" cy="48%" r="55%">
      <stop offset="0%" stop-color="#f4ede6"/>
      <stop offset="60%" stop-color="#d9b49a"/>
      <stop offset="100%" stop-color="#8a3f17"/>
    </radialGradient>
    <linearGradient id="waveTone" x1="0" y1="0" x2="0" y2="1">
      <stop offset="0%" stop-color="#217a3c" stop-opacity="0.6"/>
      <stop offset="100%" stop-color="#217a3c" stop-opacity="0"/>
    </linearGradient>
    <clipPath id="fieldClip">
      <rect x="190" y="216" width="822" height="566" rx="14"/>
    </clipPath>
  </defs>

  <rect class="sheet" x="130" y="158" width="942" height="684"/>

  <g class="tin-frame">
    <rect class="frame-brown" x="152" y="178" width="898" height="642" rx="46"/>
    <rect class="frame-lime" x="162" y="188" width="878" height="622" rx="38"/>
    <rect class="frame-brown" x="178" y="204" width="846" height="590" rx="24"/>
    <rect class="field" x="190" y="216" width="822" height="566" rx="14"/>
  </g>

  <rect role="img" aria-label="Soft band of darker green waves across the upper label"
        clip-path="url(#fieldClip)"
        x="190" y="216" width="822" height="360" fill="url(#waveTone)"/>

  <rect class="cert-badge" x="219" y="253" width="160" height="58" rx="5"/>

  <g class="mascot-medallion">
    <circle class="ring-brown" cx="592" cy="365" r="193"/>
    <circle class="ring-lime" cx="592" cy="365" r="183"/>
    <circle class="ring-brown" cx="592" cy="365" r="165"/>
    <circle class="portrait" role="img"
            aria-label="Illustration of a smiling red and white bulldog head with a brown eye patch"
            cx="592" cy="365" r="150"/>
  </g>

  <g class="organic-seal">
    <circle class="seal" cx="885" cy="347" r="112"/>
    <g transform="rotate(-8 885 347)">
      <text class="seal-text" x="885" y="340" text-anchor="middle"
            textLength="130" lengthAdjust="spacingAndGlyphs">100%</text>
      <text class="seal-text" x="885" y="398" text-anchor="middle"
            textLength="160" lengthAdjust="spacingAndGlyphs">ORGANIC</text>
    </g>
  </g>

  <text class="brand-name" x="595" y="700" text-anchor="middle"
        textLength="700" lengthAdjust="spacingAndGlyphs"
        transform="rotate(-5 595 655)">PLUMP OSCAR</text>

  <text class="product-name" x="762" y="745" text-anchor="middle"
        textLength="330" lengthAdjust="spacingAndGlyphs"
        transform="rotate(-5 762 732)">SKIN BALM</text>
</svg>
</body>
</html>
```